Spiritual Web Design Project

I am looking to rebrand our www.GlowingPathMentorInstitute.com site to have a more spiritual look and feel (find out everything we do and offer at that site - have also uploaded picture of current site).
Photoshop format is fine and then we can have someone code it for our Wordpress site.
I want the site to have more movement and light to it (but static for our Wordpress site Don't want flash) I want the site to have a warmer, more ethereal feel to it.
I like the yellow, but think it needs more 'life' and a more spiritual feel. I am also thinking of changing to purple (see a sample attached - although this is a little too dark).
Maybe the banner should go the entire width of a webpage (like this): http://www.marlowdesignhub.com/speaking
or this: http://www.trovebright.com/faqs
with a simple white background
I like this background (but not the dark blue)
http://www.tidal-wisdomnet.com/ I like this style of background, and I like this colour and style here: http://www.everydaygrowthkits.com/
I want our background to have more 'light and movement' in it.
I am thinking of changing our current font. I quite like the font here:
http://www.tidal-wisdomnet.com/
Also the two fonts attached - I like more depth (light and shade) in these than the one we have on our site now which looks quite flat
I've also attached a sample of some changes I have been looking at but I think there is too much purple
Again, I am not exactly sure what I want, but I will definately know it when I see it. The one thing I would like to keep is our 'flower graphic' on the left hand side. Also, maybe my photo could be incorporated somewhere - but not really sure if it needs to be
Once we have the branding of the site done, I want to re-brand everything else, all the resources, marketing materials etc.
Please don't submit before you look at the sites I have mentioned that I like and the attachments.
ALso I only need the Header Graphic and the Background of the site - we are doing the actual site ourselves - so I need a header and background only
Target Market(s)
Spirit-led women who are looking to start their own Law of Attraction Coaching Business
Industry/Entity Type
Marketing
Requirements
Should not have
- Flash
Should not be dark

```html
<!DOCTYPE html>
<html lang="en">
<head>
<meta charset="utf-8">
<title>Glowing Path Mentor Institute</title>
<link rel="stylesheet" href="https://fonts.googleapis.com/css2?family=Cinzel:wght@700&family=Cabin+Condensed:wght@500;700&family=Fjord+One&family=PT+Sans:wght@400;700&display=swap">
<style>
:root{
  --purple-deep:#2c1a5c;
  --purple:#3f2b72;
  --purple-btn:#3b2968;
  --violet:#7a4fc9;
  --orange:#e0870f;
  --yellow:#fcd33a;
  --yellow-dark:#f1a400;
  --grey-text:#6a6a6a;
  --rule:#dcdcdc;
  --footer-bg:#fbf8ef;
  --sky:#1a7fe0;
}
*{margin:0;padding:0;box-sizing:border-box}
html,body{width:1200px;height:2436px;overflow:hidden;background:#fff}
body{font-family:"PT Sans",sans-serif;color:var(--grey-text)}
.page{position:relative;width:1200px;height:2436px}
.abs{position:absolute}

.site-header{left:0;top:0;width:1200px;height:178px;
  background:radial-gradient(ellipse at 88% 40%,#f4eaff 0%,#c9a4ff 8%,transparent 30%),
  linear-gradient(180deg,#5b2fb5 0%,#8c5ce0 55%,#6a3dc4 100%)}
.brand{left:100px;top:38px;display:flex;align-items:center;gap:22px}
.brand-mark{width:104px;height:104px;border-radius:50%;background:#5a3bb0}
.brand-name{font-family:"Cinzel",serif;font-weight:700;font-size:42px;line-height:46px;color:#fff;letter-spacing:1px}

.main-nav{left:0;top:178px;width:1200px;height:61px;
  background:linear-gradient(180deg,var(--yellow) 0%,var(--yellow-dark) 100%);
  display:flex;align-items:center;padding-left:78px}
.main-nav a{font-family:"Cabin Condensed",sans-serif;font-weight:700;font-size:19px;color:var(--purple-deep);
  text-decoration:none;padding:0 20px;border-left:1px solid #c98a00;line-height:20px}
.main-nav a:first-child{border-left:none;padding-left:12px}

.hero{left:0;top:239px;width:1200px;height:394px;
  background:radial-gradient(circle at 56% 12%,#fff 0%,#e3f3ff 12%,transparent 32%),
  radial-gradient(ellipse at 8% 30%,#f4f8ff 0%,transparent 22%),
  radial-gradient(ellipse at 50% 55%,#f1dcc2 0%,#d3a876 10%,transparent 24%),
  linear-gradient(180deg,#57a9f0 0%,var(--sky) 100%)}
.hero-arrow{top:135px}

.intro-title{left:68px;top:668px;font-family:"Fjord One",serif;font-size:27px;color:var(--orange)}
.intro-sub{left:68px;font-size:18px;color:var(--purple-deep);font-weight:700;font-family:"Cabin Condensed",sans-serif}
.body-copy{font-size:14px;line-height:22px;color:var(--grey-text)}
.learn-more{left:68px;top:910px;font-family:"Cabin Condensed",sans-serif;font-weight:700;font-size:16px;color:var(--purple-deep);text-decoration:none}
.rule{left:65px;width:734px;height:1px;background:var(--rule)}

.feature-title{font-family:"Fjord One",serif;font-size:23px;line-height:30px;color:var(--orange)}
.btn{display:flex;align-items:center;justify-content:center;background:var(--purple-btn);color:#fff;
  font-size:13px;border-radius:3px;text-decoration:none;box-shadow:0 2px 3px rgba(0,0,0,.25)}

.testimonial-card{left:65px;width:721px;border:1px solid #e1e1e1;background:#fff;box-shadow:0 2px 4px rgba(0,0,0,.12)}
.portrait{border-radius:10px;border:2px solid #9b3434}
.testimonial-card p{font-size:14px;line-height:21px}
.testimonial-card .who{font-size:16px;color:#333;margin-top:8px}

.side-box{left:825px;width:307px;border:1px solid #dedede;background:#fff;box-shadow:0 2px 5px rgba(0,0,0,.12)}
.video{left:825px;top:666px;width:307px;height:211px;border-top:8px solid #222;border-bottom:8px solid #222;
  background:linear-gradient(90deg,#6c7a86 0%,#a9b4bd 40%,#e8eef3 65%,#c4ccd3 100%)}
.play{left:138px;top:80px;width:36px;height:36px;border-radius:50%;background:#222;display:flex;align-items:center;justify-content:center}

.signup-title{font-family:"Cabin Condensed",sans-serif;font-weight:700;font-size:25px;color:var(--purple-deep);text-align:center}
.field{left:30px;width:250px;height:31px;background:#efefef;border-radius:2px;font-size:13px;color:#666;padding:7px 12px}
.cta-yellow{display:flex;align-items:center;justify-content:center;
  background:linear-gradient(180deg,var(--yellow),var(--yellow-dark));border-radius:4px;
  font-family:"Cabin Condensed",sans-serif;font-weight:700;font-size:19px;color:var(--purple-deep)}

.box-head{background:var(--purple);color:#fff;font-family:"Fjord One",serif;font-size:21px;padding:12px 28px}
.quote{font-size:13px;line-height:23px;color:#555}
.quote-name{font-size:15px;color:#333}

.modules-title{font-family:"Fjord One",serif;font-size:19px;line-height:26px;color:var(--purple-deep);text-align:center}
.module-list{list-style:none}
.module-list li{font-size:14px;line-height:18px;color:var(--purple-deep);padding-left:20px;position:relative;margin-bottom:17px}
.module-list li::before{content:"";position:absolute;left:2px;top:4px;border-left:7px solid var(--purple-deep);border-top:5px solid transparent;border-bottom:5px solid transparent}

.join-box{left:827px;top:1986px;width:308px;height:200px;border-radius:3px;
  background:linear-gradient(180deg,var(--yellow) 0%,var(--yellow-dark) 100%);text-align:center;box-shadow:0 2px 4px rgba(0,0,0,.2)}

.site-footer{left:0;top:2257px;width:1200px;height:179px;background:var(--footer-bg);border-top:1px solid #ebe6d8}
.footer-links{left:70px;top:40px;font-size:14px;color:#222;font-weight:700}
.copyright{left:72px;top:84px;font-size:12px;color:#444}
.social{top:36px;width:32px;height:32px;border-radius:50%;background:var(--purple-deep)}
</style>
</head>
<body>
<div class="page">

  <header class="abs site-header">
    <div class="abs brand">
      <span class="brand-mark"></span>
      <span class="brand-name">GLOWING PATH<br>MENTOR INSTITUTE</span>
    </div>
  </header>

  <nav class="abs main-nav">
    <a href="#">HOME</a><a href="#">LIFE COACH</a><a href="#">ABOUT US</a><a href="#">SUCCESS STORIES</a><a href="#">MEDIA &amp; AWARDS</a><a href="#">CONTACT US</a><a href="#">COACHES LOGIN</a>
  </nav>

  <section class="abs hero" role="img" aria-label="Slideshow photo of a white dove flying upward against a bright blue sky with sun and clouds">
    <svg class="abs hero-arrow" style="left:20px" width="44" height="80" viewBox="0 0 44 80"><polyline points="38,4 6,40 38,76" fill="none" stroke="#d8d8d8" stroke-width="4"/></svg>
    <svg class="abs hero-arrow" style="left:1136px" width="44" height="80" viewBox="0 0 44 80"><polyline points="6,4 38,40 6,76" fill="none" stroke="#16507f" stroke-width="4"/></svg>
  </section>

  <h1 class="abs intro-title">Do You Love ‘The Inner Key’ and the Law of Attraction?</h1>
  <p class="abs intro-sub" style="top:707px">Want to Spend Your Days Becoming the Best You Can Be?</p>
  <p class="abs intro-sub" style="top:739px">Ready to Help Others Create an AMAZING Future AND be Paid Abundantly to Do So?</p>
  <p class="abs body-copy" style="left:68px;top:785px;width:730px">If you answered Yes – then your spirit will soar as you are about to discover how your life will be changed forever more.</p>
  <p class="abs body-copy" style="left:68px;top:837px;width:730px">Hi, my name is Rhea Calloway and I’ve transformed my life and thousands of others by using these exact principles. I became an Accredited Coach in 2001 and have created a wonderfully fulfilling and successful coaching business by combining the Law of Attraction with masterful practical strategies.</p>
  <a class="abs learn-more" href="#">LEARN MORE</a>
  <div class="abs rule" style="top:963px"></div>

  <h2 class="abs feature-title" style="left:68px;top:996px;width:340px">Glowing Path<br>Coach Certification</h2>
  <div class="abs body-copy" style="left:68px;top:1068px;width:340px">
    <p>Offers the Most Comprehensive Coach Training, Spiritual and Business Success Secrets in ONE Program Incorporating Proven Success Models WITH Law of Attraction Principles so You and Your Clients</p>
    <p style="margin-top:10px">Have the BEST Chance to Create Powerful Long-lasting Change…</p>
    <p style="margin-top:10px">And the exciting thing is… YOUR life will be transformed as you go through your training,</p>
  </div>
  <a class="abs btn" href="#" style="left:68px;top:1276px;width:174px;height:33px">Click here to learn more</a>

  <h2 class="abs feature-title" style="left:440px;top:996px;width:370px">Become an Internationally<br>Certified Glowing Path Coach if:</h2>
  <div class="abs body-copy" style="left:440px;top:1068px;width:340px">
    <p>Your spirit is calling you to do something worthwhile you love on a daily basis</p>
    <p style="margin-top:10px">You want to learn to be the best YOU possible then take that knowledge into the world to help others do the same</p>
    <p style="margin-top:10px">You want to create an additional stream of income (or a thriving business) where you are paid abundantly for helping others achieve their goals</p>
  </div>
  <a class="abs btn" href="#" style="left:443px;top:1273px;width:174px;height:33px">Click here to learn more</a>

  <div class="abs rule" style="top:1356px"></div>

  <h2 class="abs feature-title" style="left:65px;top:1380px;width:360px">How You’ll Benefit by Being an<br>Glowing Path Coach</h2>
  <p class="abs body-copy" style="left:65px;top:1448px;width:340px">On completion of your training, you’ll receive Professional Credentials as a Glowing Path Coach (and can call yourself a Certified Glowing Path Coach OR a Certified Glowing Path Law of Attraction Coach) for added credibility.</p>
  <a class="abs btn" href="#" style="left:65px;top:1593px;width:174px;height:33px">Click here to learn more</a>

  <h2 class="abs feature-title" style="left:436px;top:1380px;width:370px">In a nutshell,<br>how does the Glowing Path Coach<br>Certification program work?</h2>
  <p class="abs body-copy" style="left:436px;top:1478px;width:345px">On completion of your training, you’ll receive Professional Credentials as a Glowing Path Coach (and can call yourself a Certified Glowing Path Coach OR a Certified Glowing Path Law of Attraction Coach)</p>
  <a class="abs btn" href="#" style="left:438px;top:1593px;width:174px;height:33px">Click here to learn more</a>

  <article class="abs testimonial-card" style="top:1668px;height:219px">
    <div class="abs portrait" role="img" aria-label="Portrait photo of a smiling woman with red hair" style="left:22px;top:28px;width:96px;height:122px;background:linear-gradient(160deg,#c06a3a,#e8b89a 55%,#7a3a2a)"></div>
    <div class="abs" style="left:140px;top:28px;width:555px">
      <p>Joining the GPMI was the biggest financial risk I have ever taken in regard to doing something for myself but I have received so much more for my investment than I ever dreamed. The program itself is amazing and I absolutely love the connections and friendships I have made. I am finally doing something I am very passionate about that fills me with emotion and makes my heart sing. Thank you!!</p>
      <p class="who">Joanne P., Australia</p>
    </div>
  </article>

  <article class="abs testimonial-card" style="top:1916px;height:187px">
    <div class="abs portrait" role="img" aria-label="Portrait photo of a smiling woman with blonde hair" style="left:22px;top:21px;width:96px;height:122px;background:linear-gradient(160deg,#d8b46a,#f0d6b4 55%,#8aa060)"></div>
    <div class="abs" style="left:140px;top:26px;width:555px">
      <p>The GPMI is the best well rounded coaching course that exists!! It covers not only the actual coaching process but the spiritual and self-growth aspects and the business and marketing aspects. Am I glad I joined? Absolutely!!! No question about it!</p>
      <p class="who" style="margin-top:2px">Lena W., Australia</p>
    </div>
  </article>

  <a class="abs btn" href="#" style="left:604px;top:2129px;width:187px;height:36px;font-size:14px">View more testimonials</a>

  <aside>
    <div class="abs video" role="img" aria-label="Video thumbnail of a smiling businesswoman in an office">
      <div class="abs play"><svg width="14" height="16" viewBox="0 0 14 16"><polygon points="2,1 13,8 2,15" fill="#fff"/></svg></div>
    </div>

    <div class="abs side-box" style="top:890px;height:276px;background:linear-gradient(180deg,#fff,#f5f5f5)">
      <p class="abs signup-title" style="left:0;top:18px;width:307px">FREE COACH TRAINING</p>
      <p class="abs" style="left:0;top:56px;width:307px;text-align:center;font-size:15px;line-height:20px;color:var(--purple-deep)">Simply enter your name &amp; email<br>for instant access!</p>
      <div class="abs field" style="top:114px">First name</div>
      <div class="abs field" style="top:152px">email address</div>
      <div class="abs cta-yellow" style="left:30px;top:205px;width:250px;height:41px">GET ACCESS NOW</div>
    </div>

    <div class="abs side-box" style="top:1184px;height:450px">
      <div class="box-head">Customer Testimonials</div>
      <div class="abs" style="left:32px;top:70px;width:250px">
        <p class="quote">The GPMI has allowed me to improve my website, become a published author and have confidence in what I do. My husband is now at peace about what his retirement will look like – HUGE!!</p>
        <p class="quote-name" style="margin-top:10px">Marisa T</p>
        <p class="quote" style="margin-top:30px">I love the transformational processes and the structure the Institute offered. It enabled me to get out of my comfort zone and create a new business following my passion</p>
        <p class="quote-name" style="margin-top:10px">Delia R</p>
      </div>
      <div class="abs" style="left:0;top:400px;width:287px;height:36px;border-top:1px solid #e3e3e3;display:flex;align-items:center;justify-content:flex-end;gap:6px;font-size:14px;color:var(--purple-deep)">View more testimonials
        <svg width="8" height="10" viewBox="0 0 8 10"><polygon points="0,0 8,5 0,10" fill="#2c1a5c"/></svg></div>
    </div>

    <div class="abs side-box" style="top:1647px;height:323px">
      <div style="background:#f4f4f4;padding:14px 10px 12px;border-bottom:1px solid #e6e6e6">
        <p class="modules-title">Glowing Path Institute will<br>be guided through 6 modules:</p>
      </div>
      <ul class="abs module-list" style="left:25px;top:105px;width:270px">
        <li>Masterful Coaching Skills for Success</li>
        <li>The Key behind The Inner Key</li>
        <li>Blissful Business Building &amp; the Magic of Marketing</li>
        <li>Million Dollar Mindset Secrets</li>
        <li>Transformational Energy Processes</li>
        <li>Advanced Divine Manifesting</li>
      </ul>
    </div>

    <div class="abs join-box">
      <p style="margin-top:24px;font-family:'Cabin Condensed',sans-serif;font-weight:700;font-size:21px;color:var(--purple-deep)">Join Today – Limited Places!</p>
      <p style="margin:6px auto 0;width:262px;font-size:11px;line-height:17px;font-weight:700;color:var(--purple-deep)">Never before have we delivered such amazing bonuses Everything you need to support you to success as a Coach!</p>
      <div class="btn" style="margin:18px auto 0;width:190px;height:40px;font-family:'Cabin Condensed',sans-serif;font-weight:700;font-size:17px">CLICK HERE TO JOIN US</div>
    </div>
  </aside>

  <footer class="abs site-footer">
    <p class="abs footer-links">Affiliates | Affiliate Login | Media and Awards | Coaches Login (Previous) | Contact Us | Giving Back | Terms &amp; Conditions.</p>
    <p class="abs copyright">Copyright © 2013 Company Name.&nbsp; All right reserved.&nbsp; Term of Use</p>
    <span class="abs social" style="left:974px"></span>
    <span class="abs social" style="left:1010px"></span>
    <span class="abs social" style="left:1046px"></span>
    <span class="abs social" style="left:1082px"></span>
  </footer>

</div>
</body>
</html>
```